User Frontend Design for Support Logging System

I have a PHP web application to manage IT support calls and require a front-end design and user logon screen.

I have attached the current design which needs improving.

I have 2 current designs. The 2nd design is one I have been working on but requires a "professional touch". I also require the tables designed with dummy data from the 1st design.

I have attached my company logo in AI format which I would like incorporated into the design. There should also be a placeholder to supply the users company name upon login.

The screenshots I have attached should explain what I am looking for.

The Home Page should include charts which show statistical information such as:
Number of support tickets logged per month. Bar Chart etc.
Number of currently open support tickets.
Number of Quote Requests awaiting a response.
Number of Files and file repository.
Number of Reports.
Number of Customers.

For the Jobs and Customers pages the table fields should be designed as per the attached screenshots but a better looking tables. The table options such as uploading a file and adding a customer - these options can be changed and displayed differently.

Quotes page should display quotes returned and a "request a quote form".

Files page should have a good structure for browsing through an archive of files.

Profile page should have the option to include a profile picture.

An additional side page should be created for a web based calendar (these calendar entries will be updated by code).

The navbar should also include an alerts section.
The current attached design I have is based on bootstraps navbar.

Inspiration: http://pelvoriad.com/freebie/free-admin-templates-for-backend-panels/

Hopefully this above link will show you some navigation style designs that I am looking for.

Please note, I will be doing the PHP coding myself and it is just the page designs I require in either HTML and or PHP format. I also require the CSS files for this project.
I need the code in a format where I can add and remove items in the menu from the code and not PSD/image based format.

If you think this project requires a higher budget let me know what you would expect and I will increase it!

Any questions, please let me know.
Dummy data can be shown for design purposes.

I have provided you a dummy login to our current system to show you the system:
https://ridge.brivelnetworks.co.uk/
username: dan.prewett@brivelnetworks.co.uk
password:P@55w0rd

```html
<!DOCTYPE html>
<html lang="en">
<head>
<meta charset="utf-8">
<title>Home – Brivel Networks Support</title>
<link href="https://fonts.googleapis.com/css2?family=Open+Sans:wght@300;400;600&display=swap" rel="stylesheet">
<style>
:root{
  --blue:#2391ef;
  --white:#ffffff;
  --panel-bg:#f4f4f4;
  --line:#d9d9d9;
  --text:#222222;
  --muted:#555555;
  --grid:#f0a070;
  --grid-v:#7fbcf3;
  --badge:#2391ef;
  --avatar:#8a6a55;
}
*{box-sizing:border-box;margin:0;padding:0}
html,body{width:1200px;height:840px;overflow:hidden}
body{font-family:"Open Sans",sans-serif;color:var(--text);background:var(--white);position:relative}

/* top bar */
.topbar{position:absolute;left:0;top:0;width:1200px;height:60px;background:var(--white);border-bottom:1px solid var(--line)}
.brand{position:absolute;left:26px;top:16px;display:flex;align-items:center;gap:8px;font-size:20px;font-weight:600;color:var(--text)}
.brand-mark{width:22px;height:22px;border:2px solid var(--blue);border-radius:50%}
.tool{position:absolute;top:10px;width:39px;height:39px;border:1px solid var(--line);border-radius:50%;display:flex;align-items:center;justify-content:center;background:var(--white)}
.tool .badge{position:absolute;right:-6px;top:-3px;min-width:15px;height:15px;background:var(--badge);color:var(--white);font-size:10px;line-height:15px;text-align:center;border-radius:2px}
.user{position:absolute;left:953px;top:7px;display:flex;align-items:center;gap:8px}
.avatar{width:44px;height:44px;border-radius:50%;background:radial-gradient(circle at 50% 40%,#b88f74,var(--avatar) 60%,#3a2c24)}
.user-name{font-size:18px;color:var(--text)}
.caret{font-size:10px;margin-left:8px;color:var(--muted)}

/* sidebar */
.sidebar{position:absolute;left:0;top:60px;width:216px;height:780px;background:var(--panel-bg);border-right:1px solid var(--line)}
.menu{list-style:none;margin-top:55px}
.menu li{position:relative;height:44.5px;display:flex;align-items:center;padding-left:55px;font-size:14px;color:var(--text);border-bottom:1px solid var(--line)}
.menu li svg{position:absolute;left:19px;top:50%;transform:translateY(-50%)}
.menu li.active{background:var(--blue);color:var(--white);border-bottom-color:var(--blue)}
.menu li.active::after{content:"";position:absolute;right:-10px;top:13px;border-left:10px solid var(--blue);border-top:9px solid transparent;border-bottom:9px solid transparent}

/* page heading */
.page-head{position:absolute;left:216px;top:60px;width:984px;height:55px;background:var(--panel-bg);border-bottom:1px solid var(--line)}
.page-head h1{font-weight:300;font-size:29px;position:absolute;left:24px;top:8px}

/* stat cards */
.stat-card{position:absolute;top:153px;width:216px;height:205px;border:1px solid var(--line);background:var(--white);text-align:center}
.stat-card .icon{height:30px;margin-top:16px;display:flex;justify-content:center;align-items:center}
.stat-card .count{font-size:28px;line-height:32px;margin-top:14px}
.stat-card .label{font-size:23px;line-height:28px}
.stat-card .card-foot{position:absolute;left:0;bottom:0;width:100%;height:62px;border-top:1px solid var(--line);display:flex;justify-content:center;align-items:center}
.btn{background:var(--blue);color:var(--white);font-size:13px;width:148px;height:35px;display:flex;align-items:center;justify-content:center;border-radius:2px}

/* tickets */
.tickets{position:absolute;left:240px;top:412px;width:935px;height:329px;border:1px solid var(--line)}
.tickets-chart{position:absolute;left:0;top:0;width:601px;height:100%;border-right:1px solid var(--line)}
.tickets-chart h2{font-weight:300;font-size:29px;position:absolute;left:14px;top:13px}
.tickets-chart h2 small{font-size:18px;font-weight:400}
.chart-area{position:absolute;left:0;top:70px;width:600px;height:210px;background:var(--blue)}
.tickets-summary{position:absolute;left:601px;top:0;width:332px;height:100%;text-align:center}
.summary-item{font-size:23px;line-height:30px}
.summary-rule{width:84px;height:1px;background:var(--line);margin:18px auto 22px}
.total-box{width:196px;height:82px;background:var(--blue);color:var(--white);margin:34px auto 0;font-size:23px;line-height:30px;padding-top:11px;font-weight:300}

/* footer */
.footer{position:absolute;left:216px;top:799px;width:984px;height:41px;background:var(--panel-bg);border-top:1px solid var(--line);font-size:12px;text-align:center;line-height:39px;color:var(--text)}
</style>
</head>
<body>

<header class="topbar">
  <div class="brand"><span class="brand-mark"></span>Brivel Networks</div>

  <div class="tool" style="left:744px">
    <svg width="20" height="16" viewBox="0 0 20 16"><g fill="#333"><rect x="0" y="1" width="3" height="3"/><rect x="5" y="1" width="15" height="3"/><rect x="0" y="6.5" width="3" height="3"/><rect x="5" y="6.5" width="15" height="3"/><rect x="0" y="12" width="3" height="3"/><rect x="5" y="12" width="15" height="3"/></g></svg>
    <span class="badge">2</span>
  </div>
  <div class="tool" style="left:812px">
    <svg width="20" height="14" viewBox="0 0 20 14"><rect x="1" y="1" width="18" height="12" fill="none" stroke="#333" stroke-width="1.6"/><path d="M1 1l9 7 9-7" fill="none" stroke="#333" stroke-width="1.6"/></svg>
    <span class="badge">7</span>
  </div>
  <div class="tool" style="left:880px">
    <svg width="6" height="22" viewBox="0 0 6 22"><rect x="0.5" y="0" width="5" height="15" fill="#333"/><rect x="0.5" y="17" width="5" height="5" fill="#333"/></svg>
    <span class="badge">4</span>
  </div>

  <div class="user">
    <div class="avatar" role="img" aria-label="User profile photo"></div>
    <span class="user-name">Martin Halloway</span><span class="caret">▼</span>
  </div>
</header>

<nav class="sidebar">
  <ul class="menu">
    <li class="active"><svg width="16" height="14" viewBox="0 0 16 14"><path d="M8 1L1 7h2v6h4V9h2v4h4V7h2z" fill="none" stroke="#fff" stroke-width="1.5"/></svg>Home</li>
    <li><svg width="14" height="14" viewBox="0 0 14 14"><path d="M2 2l10 10M12 2L2 12" stroke="#222" stroke-width="2"/></svg>Jobs</li>
    <li><svg width="12" height="12" viewBox="0 0 12 12"><circle cx="6" cy="3.5" r="3" fill="#222"/><path d="M1 12c0-4 10-4 10 0z" fill="#222"/></svg>Customers</li>
    <li><svg width="14" height="14" viewBox="0 0 14 14"><rect x="1" y="1" width="12" height="12" fill="#c8d4ea"/></svg>Inventory</li>
    <li><svg width="14" height="13" viewBox="0 0 14 13"><g fill="#222"><rect x="0" y="0" width="2.5" height="13"/><rect x="4" y="3" width="2.5" height="10"/><rect x="8" y="6" width="2.5" height="7"/><rect x="11.5" y="10" width="2.5" height="3"/></g></svg>Reports</li>
    <li><svg width="11" height="14" viewBox="0 0 11 14"><path d="M0 0h7l4 4v10H0z" fill="#222"/></svg>Files</li>
    <li><svg width="14" height="11" viewBox="0 0 14 11"><path d="M0 11V5Q0 0 5 0v2Q2.5 2 2.5 5H6v6zM8 11V5q0-5 5-5v2q-2.5 0-2.5 3H14v6z" fill="#222"/></svg>Quotes</li>
  </ul>
</nav>

<div class="page-head"><h1>Home</h1></div>

<main>
  <section class="stat-card" style="left:241px">
    <div class="icon"><svg width="26" height="26" viewBox="0 0 26 26"><circle cx="13" cy="7" r="6.5" fill="var(--blue)"/><path d="M1 26c0-11 24-11 24 0z" fill="var(--blue)"/></svg></div>
    <div class="count">159</div><div class="label">Customers</div>
    <div class="card-foot"><span class="btn">View Customers</span></div>
  </section>
  <section class="stat-card" style="left:478px">
    <div class="icon"><svg width="30" height="26" viewBox="0 0 14 11"><path d="M0 11V5Q0 0 5 0v2Q2.5 2 2.5 5H6v6zM8 11V5q0-5 5-5v2q-2.5 0-2.5 3H14v6z" fill="var(--blue)"/></svg></div>
    <div class="count">35</div><div class="label">Quote Requests</div>
    <div class="card-foot"><span class="btn">View Requests</span></div>
  </section>
  <section class="stat-card" style="left:719px">
    <div class="icon"><svg width="22" height="28" viewBox="0 0 11 14"><path d="M0 0h7l4 4v10H0z" fill="var(--blue)"/></svg></div>
    <div class="count">86</div><div class="label">Files</div>
    <div class="card-foot"><span class="btn">View Files</span></div>
  </section>
  <section class="stat-card" style="left:959px">
    <div class="icon"><svg width="28" height="26" viewBox="0 0 14 13"><g fill="var(--blue)"><rect x="0" y="0" width="2.5" height="13"/><rect x="4" y="3" width="2.5" height="10"/><rect x="8" y="6" width="2.5" height="7"/><rect x="11.5" y="10" width="2.5" height="3"/></g></svg></div>
    <div class="count">32</div><div class="label">Reports</div>
    <div class="card-foot"><span class="btn">View Reports</span></div>
  </section>

  <section class="tickets">
    <div class="tickets-chart">
      <h2>Support Tickets / <small>month</small></h2>
      <div class="chart-area">
        <svg width="600" height="210" viewBox="0 0 600 210" font-family="Open Sans, sans-serif" font-size="11" fill="#fff">
          <g stroke="var(--grid-v)" stroke-width="1">
            <line x1="59" y1="24" x2="59" y2="176"/><line x1="104" y1="24" x2="104" y2="176"/><line x1="150" y1="24" x2="150" y2="176"/><line x1="196" y1="24" x2="196" y2="176"/><line x1="242" y1="24" x2="242" y2="176"/><line x1="288" y1="24" x2="288" y2="176"/><line x1="333" y1="24" x2="333" y2="176"/><line x1="379" y1="24" x2="379" y2="176"/><line x1="425" y1="24" x2="425" y2="176"/><line x1="471" y1="24" x2="471" y2="176"/><line x1="517" y1="24" x2="517" y2="176"/><line x1="563" y1="24" x2="563" y2="176"/>
          </g>
          <g stroke="var(--grid)" stroke-width="1">
            <line x1="49" y1="46" x2="576" y2="46"/><line x1="49" y1="67.5" x2="576" y2="67.5"/><line x1="49" y1="89" x2="576" y2="89"/><line x1="49" y1="111" x2="576" y2="111"/><line x1="49" y1="132.5" x2="576" y2="132.5"/><line x1="49" y1="154" x2="576" y2="154"/>
          </g>
          <line x1="49" y1="176" x2="576" y2="176" stroke="#fff"/>
          <g fill="#fff">
            <rect x="64" y="122" width="34" height="54"/><rect x="110" y="89" width="34" height="87"/><rect x="156" y="154" width="34" height="22"/><rect x="202" y="133" width="34" height="43"/><rect x="248" y="54" width="34" height="122"/><rect x="294" y="67" width="34" height="109"/><rect x="339" y="54" width="34" height="122"/><rect x="385" y="89" width="34" height="87"/><rect x="431" y="100" width="34" height="76"/><rect x="477" y="139" width="34" height="37"/><rect x="523" y="111" width="34" height="65"/>
          </g>
          <g text-anchor="end">
            <text x="39" y="180">0</text><text x="39" y="158">10</text><text x="39" y="137">20</text><text x="39" y="115">30</text><text x="39" y="93">40</text><text x="39" y="72">50</text><text x="39" y="50">60</text>
          </g>
          <g text-anchor="middle">
            <text x="81" y="194">JAN</text><text x="127" y="194">FEB</text><text x="173" y="194">MAR</text><text x="219" y="194">APR</text><text x="265" y="194">MAY</text><text x="311" y="194">JUN</text><text x="356" y="194">JUL</text><text x="402" y="194">AUG</text><text x="448" y="194">SEP</text><text x="494" y="194">OCT</text><text x="540" y="194">NOV</text>
          </g>
        </svg>
      </div>
    </div>
    <div class="tickets-summary">
      <div class="summary-item" style="margin-top:19px">34<br>Open Tickets</div>
      <div class="summary-rule"></div>
      <div class="summary-item">106<br>Resolved Tickets</div>
      <div class="total-box">140<br>Total Tickets</div>
    </div>
  </section>
</main>

<footer class="footer">Copyright © 2014 Ridge</footer>

</body>
</html>
```